Business Card for TOV

We need a Corporate style business card for a new Industrial recycling company based in Australia. We recycle industrial products from Mining companies, power stations and other large industry all around the country.

We want the card to represent a modern, innovative professional company that is an industry leader.

We want the card to be double sided. I think with the logo centred by itself on one side and the text displayed with all our details on the other side.

(or you could put the persons name with the job title on the side with the logo?? I'll leave that up to your creative sides)

Open to how you divide and place the information on the one side of the card.

I think the persons name and the title should have its own place. The rest of the information can be placed as you think is best and then I will provide feedback as to what I think works best.

I have attached the logo file so you can add that to the one side. Whether you use it in a smaller form on the second side too is an option but I'll leave that up to you initially?

Information required on the card is as follows

Dermot Halloran
Director

0438 972 506

dermot@tovq.com.au

Po Box 782
Brindle ACT 2694

www.tovq.com.au

ACN 582 917 306 (This can be in very small print and can be in the bottom corner of the card or somewhere not very prominent

Wanted to thank everyone for their submissions. 

We were really torn on about 5 designs in the end.

We decided to go with the first one we liked.

We have another company that is going to need logo and business card design in the coming weeks.

I will save your designer ID's so I can invite you all to that project. too!

Thanks again and all the best

Dermot

Target Market(s)

Corporate and medium to large business clients

Industry/Entity Type

Industrial

```html
<!DOCTYPE html>
<html lang="en">
<head>
<meta charset="utf-8">
<title>TOV Business Card</title>
<link rel="stylesheet" href="https://fonts.googleapis.com/css2?family=Exo+2:wght@400;600;800&display=swap">
<style>
  :root {
    --backdrop: #8a8a8a;
    --paper: #ffffff;
    --ink: #2b2b2b;
    --blue: #1f8fc4;
    --blue-light: #2fb0e6;
    --blue-deep: #176f9e;
    --green: #3f9e3a;
    --green-light: #7cc242;
    --brand-green: #3a9a3c;
    --row: rgba(0, 0, 0, 0.12);
    --row-edge: rgba(255, 255, 255, 0.28);
    --text-light: #ffffff;
  }
  * { box-sizing: border-box; margin: 0; padding: 0; }
  html, body { width: 1200px; height: 1200px; overflow: hidden; }
  body {
    background: var(--backdrop);
    font-family: "Exo 2", sans-serif;
    position: relative;
  }
  .card {
    position: absolute;
    top: 250px;
    width: 400px;
    height: 700px;
    background: var(--paper);
    overflow: hidden;
    box-shadow: 0 8px 24px rgba(0, 0, 0, 0.3);
  }
  .card--social { left: 150px; }
  .card--contact { left: 650px; }

  .brand {
    position: absolute;
    left: 0; right: 0;
    display: flex;
    align-items: center;
    justify-content: center;
    gap: 16px;
  }
  .card--social .brand { top: 110px; }
  .card--contact .brand { top: 80px; }
  .brand__mark {
    width: 54px; height: 54px;
    border-radius: 50%;
    background: var(--brand-green);
  }
  .brand__name {
    font-weight: 800;
    font-size: 52px;
    letter-spacing: 4px;
    color: var(--ink);
    line-height: 1;
  }

  .band { position: absolute; left: 0; right: 0; }
  .band--blue {
    background: radial-gradient(ellipse at 50% 60%, var(--blue-light), var(--blue) 55%, var(--blue-deep));
  }
  .band--green {
    background: radial-gradient(ellipse at 50% 50%, var(--green-light), var(--green) 70%);
  }

  .row {
    position: absolute;
    left: 40px; right: 40px;
    height: 44px;
    display: flex;
    align-items: center;
    gap: 14px;
    padding-left: 8px;
    background: var(--row);
    border-radius: 3px;
    color: var(--text-light);
    font-size: 19px;
    letter-spacing: 0.5px;
  }
  .row__icon {
    flex: none;
    width: 30px; height: 30px;
    border: 2px solid var(--row-edge);
    border-radius: 4px;
    display: flex;
    align-items: center;
    justify-content: center;
  }
  .row__icon svg { width: 18px; height: 18px; }
  .row__dot {
    width: 12px; height: 12px;
    background: var(--text-light);
    border-radius: 2px;
  }
  .row--tall { height: 70px; align-items: flex-start; padding-top: 7px; line-height: 1.45; }

  .person {
    position: absolute;
    top: 28px; left: 0; right: 0;
    text-align: center;
  }
  .person__name {
    font-weight: 600;
    font-size: 24px;
    letter-spacing: 1.5px;
    color: var(--text-light);
    text-transform: uppercase;
  }
  .person__title {
    font-size: 15px;
    letter-spacing: 2px;
    color: var(--text-light);
    text-transform: uppercase;
    margin-top: 2px;
  }
  .company-number {
    position: absolute;
    right: 18px; bottom: 14px;
    font-size: 11px;
    letter-spacing: 0.5px;
    color: rgba(255, 255, 255, 0.8);
  }
</style>
</head>
<body>

  <section class="card card--social">
    <div class="brand">
      <span class="brand__mark"></span>
      <span class="brand__name">TOV</span>
    </div>

    <div class="band band--blue" style="top:290px;height:160px;">
      <div class="row" style="top:58px;">
        <span class="row__icon"><span class="row__dot"></span></span>
        <span>news.tovq.com.au</span>
      </div>
    </div>
    <div class="band band--green" style="top:450px;height:115px;">
      <div class="row" style="top:36px;">
        <span class="row__icon"><span class="row__dot"></span></span>
        <span>feed.tovq.com.au</span>
      </div>
    </div>
    <div class="band band--blue" style="top:565px;height:135px;">
      <div class="row" style="top:40px;">
        <span class="row__icon"><span class="row__dot"></span></span>
        <span>team.tovq.com.au</span>
      </div>
    </div>
  </section>

  <section class="card card--contact">
    <div class="brand">
      <span class="brand__mark"></span>
      <span class="brand__name">TOV</span>
    </div>

    <div class="band band--green" style="top:230px;height:200px;">
      <div class="person">
        <div class="person__name">Dermot Halloran</div>
        <div class="person__title">Director</div>
      </div>
      <div class="row" style="top:96px;">
        <span class="row__icon">
          <svg viewBox="0 0 24 24" fill="#fff"><path d="M6.6 10.8a15.1 15.1 0 0 0 6.6 6.6l2.2-2.2a1 1 0 0 1 1-.25 11.4 11.4 0 0 0 3.6.57 1 1 0 0 1 1 1V20a1 1 0 0 1-1 1A17 17 0 0 1 3 4a1 1 0 0 1 1-1h3.5a1 1 0 0 1 1 1c0 1.25.2 2.45.57 3.57a1 1 0 0 1-.25 1z"/></svg>
        </span>
        <span>0438 972 506</span>
      </div>
      <div class="row" style="top:148px;">
        <span class="row__icon">
          <svg viewBox="0 0 24 24" fill="none" stroke="#fff" stroke-width="2"><rect x="3" y="5" width="18" height="14" rx="1"/><path d="M3 6l9 7 9-7"/></svg>
        </span>
        <span>dermot@tovq.com.au</span>
      </div>
    </div>

    <div class="band band--blue" style="top:430px;height:270px;">
      <div class="row" style="top:34px;">
        <span class="row__icon">
          <svg viewBox="0 0 24 24" fill="none" stroke="#fff" stroke-width="2"><circle cx="12" cy="12" r="9"/><path d="M3 12h18M12 3c3 3 3 15 0 18M12 3c-3 3-3 15 0 18"/></svg>
        </span>
        <span>www.tovq.com.au</span>
      </div>
      <div class="row row--tall" style="top:92px;">
        <span class="row__icon">
          <svg viewBox="0 0 24 24" fill="#fff"><path d="M12 2a7 7 0 0 0-7 7c0 5 7 13 7 13s7-8 7-13a7 7 0 0 0-7-7zm0 9.5A2.5 2.5 0 1 1 12 6.5a2.5 2.5 0 0 1 0 5z"/></svg>
        </span>
        <span>Po Box 782<br>Brindle ACT 2694</span>
      </div>
      <div class="company-number">ACN 582 917 306</div>
    </div>
  </section>

</body>
</html>
```